Poster Design For Obstacle Run

Design a poster for the Crow Ridge Obstacle run.
Text: Crow Ridge Obstacle Run. May 12th, 2018. Sittard. www.crowridgedash.nl. I have added a lot of pictures.
Furthermore, the logo should be included. As an example I included a poster from the ironbark race that we really like (ironbark team challenge) and also. Feel free to take a look at our website for inspiration: www.crowridgedash.nl

```html
<!DOCTYPE html>
<html lang="en">
<head>
<meta charset="utf-8">
<title>Crow Ridge Obstacle Run – Poster</title>
<link href="https://fonts.googleapis.com/css2?family=Rubik+Dirt&family=Roboto:wght@700&display=swap" rel="stylesheet">
<style>
  :root {
    --page-bg: #e9e9ec;
    --mud-orange: #c9531f;
    --mud-bright: #d9683a;
    --mud-dark: #5a2410;
    --wood-shadow: #3a1a0c;
    --sky-green: #6f8a5a;
    --ink: #141110;
    --paper: #ffffff;
  }
  html, body {
    margin: 0;
    padding: 0;
    width: 1018px;
    height: 1200px;
    overflow: hidden;
    background: var(--page-bg);
  }
  .poster {
    position: absolute;
    left: 99px;
    top: 26px;
    width: 820px;
    height: 1148px;
    overflow: hidden;
    background: var(--ink);
  }
  .hero-photo {
    position: absolute;
    left: 0;
    top: 0;
    width: 820px;
    height: 930px;
    background:
      linear-gradient(180deg, rgba(20,17,16,0) 62%, rgba(20,17,16,0.75) 85%, rgba(20,17,16,1) 100%),
      radial-gradient(ellipse 260px 340px at 700px 600px, rgba(217,104,58,0.85), rgba(217,104,58,0) 100%),
      radial-gradient(ellipse 180px 220px at 660px 60px, rgba(111,138,90,0.55), rgba(111,138,90,0) 100%),
      radial-gradient(ellipse 320px 160px at 300px 560px, rgba(58,26,12,0.7), rgba(58,26,12,0) 100%),
      linear-gradient(150deg, #b4552b 0%, #9c4422 22%, #c2693f 40%, #8e3a1a 58%, #b4502a 75%, #5a2410 100%);
  }
  .event-mark {
    position: absolute;
    left: 265px;
    top: 712px;
    width: 300px;
    height: 186px;
    border-radius: 50%;
    background: var(--ink);
    display: flex;
    flex-direction: column;
    align-items: center;
    justify-content: center;
    text-align: center;
  }
  .event-mark__city {
    font-family: "Roboto", Arial, sans-serif;
    font-weight: 700;
    font-size: 11px;
    letter-spacing: 4px;
    color: var(--paper);
    text-transform: uppercase;
    margin-bottom: 6px;
  }
  .event-mark__name {
    font-family: "Roboto", Arial, sans-serif;
    font-weight: 700;
    font-size: 20px;
    line-height: 1.2;
    letter-spacing: 1px;
    color: var(--paper);
    text-transform: uppercase;
  }
  .info-band {
    position: absolute;
    left: 0;
    top: 890px;
    width: 820px;
    height: 258px;
  }
  .info-band svg {
    position: absolute;
    left: 0;
    top: 0;
  }
  .info-band__title {
    position: absolute;
    left: 0;
    right: 0;
    top: 46px;
    margin: 0;
    text-align: center;
    font-family: "Rubik Dirt", Impact, sans-serif;
    font-weight: 400;
    font-size: 80px;
    line-height: 1;
    letter-spacing: 1px;
    color: var(--paper);
  }
  .info-band__details {
    position: absolute;
    left: 0;
    right: 0;
    top: 150px;
    margin: 0;
    text-align: center;
    font-family: "Roboto", Arial, sans-serif;
    font-weight: 700;
    font-size: 35px;
    color: var(--paper);
    white-space: nowrap;
  }
  .info-band__divider {
    margin: 0 30px;
  }
</style>
</head>
<body>
  <main class="poster">
    <div class="hero-photo" role="img" aria-label="Photo: mud-covered runner gripping a rope while climbing a slanted wooden wall"></div>

    <div class="event-mark">
      <span class="event-mark__city">Sittard</span>
      <span class="event-mark__name">Crow Ridge<br>Obstacle Run</span>
    </div>

    <section class="info-band">
      <svg width="820" height="258" viewBox="0 0 820 258" aria-hidden="true">
        <polygon fill="var(--mud-orange)"
          points="0,18 40,12 80,20 130,8 175,17 230,6 290,15 340,10 400,19 455,7 510,16 560,9 620,18 680,8 730,15 780,10 820,17 820,236 770,229 720,238 660,227 600,237 540,229 480,239 420,228 360,238 300,230 240,239 180,228 120,238 60,230 0,237"/>
      </svg>
      <h1 class="info-band__title">OBSTACLE RUN</h1>
      <p class="info-band__details">MAY 12TH, 2018<span class="info-band__divider">|</span>www.crowridgedash.nl</p>
    </section>
  </main>
</body>
</html>
```